Step and Repeat Backdrop for wedding reception photo booth

Would like to have a Step and Repeat Backdrop (8 foot high by 10 foot wide) that incorporates the wedding logo (attached) and the names Elena and Gavin. Background should be white, and wedding colors are burgundy and gold. Show me creativity :-) I have included some random samples.

```html
<!DOCTYPE html>
<html lang="en">
<head>
<meta charset="utf-8">
<title>Elena &amp; Gavin – Step and Repeat Backdrop</title>
<link href="https://fonts.googleapis.com/css2?family=Abril+Fatface&display=swap" rel="stylesheet">
<style>
  :root {
    --paper: #f7f8f9;
    --paper-light: #ffffff;
    --paper-shade: #eceef0;
    --burgundy: #8a1426;
    --burgundy-bright: #9b1c35;
    --burgundy-deep: #7a0f1e;
    --rose: #c9435f;
    --gold: #b8955a;
    --gold-deep: #9e7a3f;
    --gold-pale: #efe4cf;
    --gold-soft: #e3d2b0;
  }
  html, body {
    margin: 0;
    padding: 0;
    width: 1200px;
    height: 960px;
    overflow: hidden;
  }
  .backdrop {
    position: relative;
    width: 1200px;
    height: 960px;
    background: linear-gradient(135deg, var(--paper-light) 0%, var(--paper) 35%, var(--paper-shade) 55%, var(--paper) 70%, var(--paper-light) 100%);
    font-family: "Abril Fatface", "Times New Roman", serif;
  }
  .repeat-row {
    position: absolute;
    left: 54px;
    display: grid;
    grid-template-columns: repeat(9, 120.4px);
    height: 116px;
    margin-top: -58px;
  }
  .row-1 { top: 96px; }
  .row-2 { top: 200px; }
  .row-3 { top: 314px; }
  .row-4 { top: 419px; }
  .row-5 { top: 533px; }
  .row-6 { top: 637px; }
  .row-7 { top: 751px; }
  .row-8 { top: 857px; }
  .cell {
    position: relative;
    display: flex;
    align-items: center;
    justify-content: center;
    text-align: center;
  }
  .couple-names {
    margin: 0;
    font-size: 24px;
    line-height: 24px;
    color: var(--burgundy-deep);
  }
  .couple-names span { display: block; }
  .repeat-row.alt .couple-names { color: var(--burgundy-bright); }
  .repeat-row.alt .couple-names.edge,
  .couple-names.edge { color: var(--burgundy-deep); }
  .repeat-row .couple-names.rose { color: var(--rose); }
  .monogram-frame {
    position: absolute;
    left: 50%;
    top: 50%;
    width: 111px;
    height: 114px;
    margin: -57px 0 0 -55.5px;
    border-radius: 10px;
    background: radial-gradient(ellipse at center, var(--gold-soft) 0%, var(--gold-pale) 70%, rgba(239, 228, 207, 0.6) 100%);
  }
  .wedding-mark {
    position: relative;
    margin: 0;
    font-size: 22px;
    line-height: 23px;
    color: var(--gold-deep);
  }
  .wedding-mark span { display: block; }
</style>
</head>
<body>
<main class="backdrop">

  <div class="repeat-row row-1">
    <div class="cell"><div class="monogram-frame" role="img" aria-label="Gold ornamental flourish frame of the wedding monogram"></div><p class="wedding-mark"><span>Elena</span><span>&amp;</span><span>Gavin</span></p></div>
    <div class="cell"><p class="couple-names"><span>Elena</span><span>&amp;</span><span>Gavin</span></p></div>
    <div class="cell"><div class="monogram-frame" role="img" aria-label="Gold ornamental flourish frame of the wedding monogram"></div><p class="wedding-mark"><span>Elena</span><span>&amp;</span><span>Gavin</span></p></div>
    <div class="cell"><p class="couple-names"><span>Elena</span><span>&amp;</span><span>Gavin</span></p></div>
    <div class="cell"><div class="monogram-frame" role="img" aria-label="Gold ornamental flourish frame of the wedding monogram"></div><p class="wedding-mark"><span>Elena</span><span>&amp;</span><span>Gavin</span></p></div>
    <div class="cell"><p class="couple-names"><span>Elena</span><span>&amp;</span><span>Gavin</span></p></div>
    <div class="cell"><div class="monogram-frame" role="img" aria-label="Gold ornamental flourish frame of the wedding monogram"></div><p class="wedding-mark"><span>Elena</span><span>&amp;</span><span>Gavin</span></p></div>
    <div class="cell"><p class="couple-names"><span>Elena</span><span>&amp;</span><span>Gavin</span></p></div>
    <div class="cell"><div class="monogram-frame" role="img" aria-label="Gold ornamental flourish frame of the wedding monogram"></div><p class="wedding-mark"><span>Elena</span><span>&amp;</span><span>Gavin</span></p></div>
  </div>

  <div class="repeat-row row-2 alt">
    <div class="cell"><p class="couple-names edge"><span>Elena</span><span>&amp;</span><span>Gavin</span></p></div>
    <div class="cell"><div class="monogram-frame" role="img" aria-label="Gold ornamental flourish frame of the wedding monogram"></div><p class="wedding-mark"><span>Elena</span><span>&amp;</span><span>Gavin</span></p></div>
    <div class="cell"><p class="couple-names"><span>Elena</span><span>&amp;</span><span>Gavin</span></p></div>
    <div class="cell"><div class="monogram-frame" role="img" aria-label="Gold ornamental flourish frame of the wedding monogram"></div><p class="wedding-mark"><span>Elena</span><span>&amp;</span><span>Gavin</span></p></div>
    <div class="cell"><p class="couple-names"><span>Elena</span><span>&amp;</span><span>Gavin</span></p></div>
    <div class="cell"><div class="monogram-frame" role="img" aria-label="Gold ornamental flourish frame of the wedding monogram"></div><p class="wedding-mark"><span>Elena</span><span>&amp;</span><span>Gavin</span></p></div>
    <div class="cell"><p class="couple-names"><span>Elena</span><span>&amp;</span><span>Gavin</span></p></div>
    <div class="cell"><div class="monogram-frame" role="img" aria-label="Gold ornamental flourish frame of the wedding monogram"></div><p class="wedding-mark"><span>Elena</span><span>&amp;</span><span>Gavin</span></p></div>
    <div class="cell"><p class="couple-names edge"><span>Elena</span><span>&amp;</span><span>Gavin</span></p></div>
  </div>

  <div class="repeat-row row-3 alt">
    <div class="cell"><div class="monogram-frame" role="img" aria-label="Gold ornamental flourish frame of the wedding monogram"></div><p class="wedding-mark"><span>Elena</span><span>&amp;</span><span>Gavin</span></p></div>
    <div class="cell"><p class="couple-names"><span>Elena</span><span>&amp;</span><span>Gavin</span></p></div>
    <div class="cell"><div class="monogram-frame" role="img" aria-label="Gold ornamental flourish frame of the wedding monogram"></div><p class="wedding-mark"><span>Elena</span><span>&amp;</span><span>Gavin</span></p></div>
    <div class="cell"><p class="couple-names"><span>Elena</span><span>&amp;</span><span>Gavin</span></p></div>
    <div class="cell"><div class="monogram-frame" role="img" aria-label="Gold ornamental flourish frame of the wedding monogram"></div><p class="wedding-mark"><span>Elena</span><span>&amp;</span><span>Gavin</span></p></div>
    <div class="cell"><p class="couple-names"><span>Elena</span><span>&amp;</span><span>Gavin</span></p></div>
    <div class="cell"><div class="monogram-frame" role="img" aria-label="Gold ornamental flourish frame of the wedding monogram"></div><p class="wedding-mark"><span>Elena</span><span>&amp;</span><span>Gavin</span></p></div>
    <div class="cell"><p class="couple-names"><span>Elena</span><span>&amp;</span><span>Gavin</span></p></div>
    <div class="cell"><div class="monogram-frame" role="img" aria-label="Gold ornamental flourish frame of the wedding monogram"></div><p class="wedding-mark"><span>Elena</span><span>&amp;</span><span>Gavin</span></p></div>
  </div>

  <div class="repeat-row row-4 alt">
    <div class="cell"><p class="couple-names edge"><span>Elena</span><span>&amp;</span><span>Gavin</span></p></div>
    <div class="cell"><div class="monogram-frame" role="img" aria-label="Gold ornamental flourish frame of the wedding monogram"></div><p class="wedding-mark"><span>Elena</span><span>&amp;</span><span>Gavin</span></p></div>
    <div class="cell"><p class="couple-names"><span>Elena</span><span>&amp;</span><span>Gavin</span></p></div>
    <div class="cell"><div class="monogram-frame" role="img" aria-label="Gold ornamental flourish frame of the wedding monogram"></div><p class="wedding-mark"><span>Elena</span><span>&amp;</span><span>Gavin</span></p></div>
    <div class="cell"><p class="couple-names rose"><span>Elena</span><span>&amp;</span><span>Gavin</span></p></div>
    <div class="cell"><div class="monogram-frame" role="img" aria-label="Gold ornamental flourish frame of the wedding monogram"></div><p class="wedding-mark"><span>Elena</span><span>&amp;</span><span>Gavin</span></p></div>
    <div class="cell"><p class="couple-names"><span>Elena</span><span>&amp;</span><span>Gavin</span></p></div>
    <div class="cell"><div class="monogram-frame" role="img" aria-label="Gold ornamental flourish frame of the wedding monogram"></div><p class="wedding-mark"><span>Elena</span><span>&amp;</span><span>Gavin</span></p></div>
    <div class="cell"><p class="couple-names edge"><span>Elena</span><span>&amp;</span><span>Gavin</span></p></div>
  </div>

  <div class="repeat-row row-5 alt">
    <div class="cell"><div class="monogram-frame" role="img" aria-label="Gold ornamental flourish frame of the wedding monogram"></div><p class="wedding-mark"><span>Elena</span><span>&amp;</span><span>Gavin</span></p></div>
    <div class="cell"><p class="couple-names"><span>Elena</span><span>&amp;</span><span>Gavin</span></p></div>
    <div class="cell"><div class="monogram-frame" role="img" aria-label="Gold ornamental flourish frame of the wedding monogram"></div><p class="wedding-mark"><span>Elena</span><span>&amp;</span><span>Gavin</span></p></div>
    <div class="cell"><p class="couple-names rose"><span>Elena</span><span>&amp;</span><span>Gavin</span></p></div>
    <div class="cell"><div class="monogram-frame" role="img" aria-label="Gold ornamental flourish frame of the wedding monogram"></div><p class="wedding-mark"><span>Elena</span><span>&amp;</span><span>Gavin</span></p></div>
    <div class="cell"><p class="couple-names rose"><span>Elena</span><span>&amp;</span><span>Gavin</span></p></div>
    <div class="cell"><div class="monogram-frame" role="img" aria-label="Gold ornamental flourish frame of the wedding monogram"></div><p class="wedding-mark"><span>Elena</span><span>&amp;</span><span>Gavin</span></p></div>
    <div class="cell"><p class="couple-names"><span>Elena</span><span>&amp;</span><span>Gavin</span></p></div>
    <div class="cell"><div class="monogram-frame" role="img" aria-label="Gold ornamental flourish frame of the wedding monogram"></div><p class="wedding-mark"><span>Elena</span><span>&amp;</span><span>Gavin</span></p></div>
  </div>

  <div class="repeat-row row-6 alt">
    <div class="cell"><p class="couple-names edge"><span>Elena</span><span>&amp;</span><span>Gavin</span></p></div>
    <div class="cell"><div class="monogram-frame" role="img" aria-label="Gold ornamental flourish frame of the wedding monogram"></div><p class="wedding-mark"><span>Elena</span><span>&amp;</span><span>Gavin</span></p></div>
    <div class="cell"><p class="couple-names"><span>Elena</span><span>&amp;</span><span>Gavin</span></p></div>
    <div class="cell"><div class="monogram-frame" role="img" aria-label="Gold ornamental flourish frame of the wedding monogram"></div><p class="wedding-mark"><span>Elena</span><span>&amp;</span><span>Gavin</span></p></div>
    <div class="cell"><p class="couple-names"><span>Elena</span><span>&amp;</span><span>Gavin</span></p></div>
    <div class="cell"><div class="monogram-frame" role="img" aria-label="Gold ornamental flourish frame of the wedding monogram"></div><p class="wedding-mark"><span>Elena</span><span>&amp;</span><span>Gavin</span></p></div>
    <div class="cell"><p class="couple-names"><span>Elena</span><span>&amp;</span><span>Gavin</span></p></div>
    <div class="cell"><div class="monogram-frame" role="img" aria-label="Gold ornamental flourish frame of the wedding monogram"></div><p class="wedding-mark"><span>Elena</span><span>&amp;</span><span>Gavin</span></p></div>
    <div class="cell"><p class="couple-names edge"><span>Elena</span><span>&amp;</span><span>Gavin</span></p></div>
  </div>

  <div class="repeat-row row-7 alt">
    <div class="cell"><div class="monogram-frame" role="img" aria-label="Gold ornamental flourish frame of the wedding monogram"></div><p class="wedding-mark"><span>Elena</span><span>&amp;</span><span>Gavin</span></p></div>
    <div class="cell"><p class="couple-names"><span>Elena</span><span>&amp;</span><span>Gavin</span></p></div>
    <div class="cell"><div class="monogram-frame" role="img" aria-label="Gold ornamental flourish frame of the wedding monogram"></div><p class="wedding-mark"><span>Elena</span><span>&amp;</span><span>Gavin</span></p></div>
    <div class="cell"><p class="couple-names"><span>Elena</span><span>&amp;</span><span>Gavin</span></p></div>
    <div class="cell"><div class="monogram-frame" role="img" aria-label="Gold ornamental flourish frame of the wedding monogram"></div><p class="wedding-mark"><span>Elena</span><span>&amp;</span><span>Gavin</span></p></div>
    <div class="cell"><p class="couple-names"><span>Elena</span><span>&amp;</span><span>Gavin</span></p></div>
    <div class="cell"><div class="monogram-frame" role="img" aria-label="Gold ornamental flourish frame of the wedding monogram"></div><p class="wedding-mark"><span>Elena</span><span>&amp;</span><span>Gavin</span></p></div>
    <div class="cell"><p class="couple-names"><span>Elena</span><span>&amp;</span><span>Gavin</span></p></div>
    <div class="cell"><div class="monogram-frame" role="img" aria-label="Gold ornamental flourish frame of the wedding monogram"></div><p class="wedding-mark"><span>Elena</span><span>&amp;</span><span>Gavin</span></p></div>
  </div>

  <div class="repeat-row row-8">
    <div class="cell"><p class="couple-names"><span>Elena</span><span>&amp;</span><span>Gavin</span></p></div>
    <div class="cell"><div class="monogram-frame" role="img" aria-label="Gold ornamental flourish frame of the wedding monogram"></div><p class="wedding-mark"><span>Elena</span><span>&amp;</span><span>Gavin</span></p></div>
    <div class="cell"><p class="couple-names"><span>Elena</span><span>&amp;</span><span>Gavin</span></p></div>
    <div class="cell"><div class="monogram-frame" role="img" aria-label="Gold ornamental flourish frame of the wedding monogram"></div><p class="wedding-mark"><span>Elena</span><span>&amp;</span><span>Gavin</span></p></div>
    <div class="cell"><p class="couple-names"><span>Elena</span><span>&amp;</span><span>Gavin</span></p></div>
    <div class="cell"><div class="monogram-frame" role="img" aria-label="Gold ornamental flourish frame of the wedding monogram"></div><p class="wedding-mark"><span>Elena</span><span>&amp;</span><span>Gavin</span></p></div>
    <div class="cell"><p class="couple-names"><span>Elena</span><span>&amp;</span><span>Gavin</span></p></div>
    <div class="cell"><div class="monogram-frame" role="img" aria-label="Gold ornamental flourish frame of the wedding monogram"></div><p class="wedding-mark"><span>Elena</span><span>&amp;</span><span>Gavin</span></p></div>
    <div class="cell"><p class="couple-names"><span>Elena</span><span>&amp;</span><span>Gavin</span></p></div>
  </div>

</main>
</body>
</html>
```